User help guide for software for investment bank

We need a professional design for our user help guides for new software we have written for our client. We develop visualization software for investment banks in Singapore mainly focused in the financial and risk management area. Our help guides are design to show them how the software works as well as promote our brand
Updates

Project Deadline Extended Reason: I am looking for more alternative designs and we have around 10 more documents to do after this Added Saturday, November 21, 2015

Target Market(s)

Investment banking, risk management, finance

Industry/Entity Type

Bank

Requirements
Must have
• Content of document and logos
• Colour sheme
• Professional brouchure design
• Quorvin and bimsot logos on it
• Look at www.quorvin-example.com for company looks and feel
• PLEASE USE COLOUR SCHEMES BELOW IN ATTACHMENT AND FOLLOW SIMILAR STYLE TO CLIENT ANNUAL REPORT

```html
<!DOCTYPE html>
<html lang="en">
<head>
<meta charset="utf-8">
<title>Web Editing Tool – User Guide</title>
<link href="https://fonts.googleapis.com/css2?family=Jost:wght@400;500;600&display=swap" rel="stylesheet">
<style>
  :root {
    --brand-red: #d6232e;
    --ink: #111111;
    --rule: #c8c8c8;
    --paper: #ffffff;
  }
  * { box-sizing: border-box; margin: 0; padding: 0; }
  html, body { width: 848px; height: 1200px; overflow: hidden; background: var(--paper); }
  body { font-family: "Jost", "Futura", sans-serif; color: var(--ink); position: relative; }

  .title-band {
    position: absolute; left: 0; top: 0; width: 848px; height: 176px;
    background: var(--brand-red);
  }
  .title-band h1 {
    position: absolute; left: 0; right: 0; top: 102px;
    text-align: center; color: var(--paper);
    font-weight: 500; font-size: 43px; line-height: 1; letter-spacing: 0.3px;
  }

  .record-heading {
    position: absolute; left: 63px; top: 185px;
    font-size: 17px; font-weight: 500;
  }

  .record-table {
    position: absolute; left: 63px; top: 217px; width: 715px;
    border-collapse: collapse; font-size: 12px;
  }
  .record-table td, .record-table th {
    border: 1px solid var(--rule); height: 28px; padding: 0 6px;
    text-align: left; vertical-align: middle; font-weight: 400;
  }
  .record-table .label,
  .record-table th {
    background: var(--ink); color: var(--paper); font-weight: 600;
  }
  .record-table th { height: 27px; }

  .contents-band {
    position: absolute; left: 0; top: 399px; width: 375px; height: 36px;
    background: var(--brand-red); color: var(--paper);
    font-size: 20px; font-weight: 500; padding-left: 63px; line-height: 36px;
  }

  .toc { list-style: none; }
  .toc li {
    position: absolute; display: flex; align-items: baseline;
    font-size: 15.5px; line-height: 20px; white-space: nowrap;
  }
  .toc .main { font-weight: 600; }
  .toc .plain { font-weight: 400; }
  .toc .leader { flex: 1; overflow: hidden; margin: 0 2px; }
  .toc .leader::after {
    content: "..............................................................................................................................................................................................................................................";
    letter-spacing: 0.5px;
  }
</style>
</head>
<body>
  <header class="title-band">
    <h1>Web Editing Tool</h1>
  </header>

  <h2 class="record-heading">Issue / Amendment Record</h2>

  <table class="record-table">
    <colgroup>
      <col style="width:115px"><col style="width:107px"><col style="width:110px">
      <col style="width:107px"><col style="width:108px"><col style="width:168px">
    </colgroup>
    <tr><td class="label" colspan="2">Project ID</td><td colspan="4">KRSC – Credit Risk LRTM 27104856</td></tr>
    <tr><td class="label" colspan="2">Project Name</td><td colspan="4">LRTM Wholesale/ Structured Finance Templates Automation</td></tr>
    <tr><td class="label" colspan="2">Document Status</td><td colspan="4"></td></tr>
    <tr><th>Version</th><th>Date</th><th>Author</th><th>Reviewer</th><th>Approver</th><th>Version Summary</th></tr>
    <tr><td>0.1</td><td>19/11/2015</td><td>Lena Ostrova</td><td>Lena Ostrova</td><td></td><td>Initial draft</td></tr>
  </table>

  <h2 class="contents-band">Contents</h2>

  <ol class="toc">
    <li class="main" style="left:63px;top:455px;width:635px"><span>User Roles and Permissions</span><span class="leader"></span><span>3</span></li>
    <li class="main" style="left:63px;top:486px;width:635px"><span>Restrictions using Web Editor Tool</span><span class="leader"></span><span>3</span></li>
    <li class="main" style="left:63px;top:518px;width:690px"><span>Navigation</span><span class="leader"></span><span>4</span></li>
    <li class="main" style="left:91px;top:549px;width:535px"><span>Data and Analytics pane</span><span class="leader"></span><span>5</span></li>
    <li class="plain" style="left:120px;top:580px;width:506px"><span>Data Pane</span><span class="leader"></span><span>5</span></li>
    <li class="plain" style="left:120px;top:612px;width:506px"><span>Analytics pane</span><span class="leader"></span><span>6</span></li>
    <li class="main" style="left:91px;top:643px;width:535px"><span>TOOLBAR</span><span class="leader"></span><span>6</span></li>
    <li class="main" style="left:91px;top:674px;width:535px"><span>Columns and Rows</span><span class="leader"></span><span>7</span></li>
    <li class="main" style="left:91px;top:706px;width:535px"><span>Marks</span><span class="leader"></span><span>8</span></li>
    <li class="main" style="left:91px;top:737px;width:535px"><span>FILTERS</span><span class="leader"></span><span>9</span></li>
    <li class="main" style="left:63px;top:768px;width:650px"><span>Calculated Fields (Advanced)</span><span class="leader"></span><span>10</span></li>
    <li class="plain" style="left:63px;top:800px;width:570px"><span>EDIT CURRENT CALCULATED FIELDS</span><span class="leader"></span><span>10</span></li>
    <li class="plain" style="left:63px;top:831px;width:570px"><span>CREATE NEW CALCLATED FIELD</span><span class="leader"></span><span>11</span></li>
  </ol>
</body>
</html>
```